Corwen Haddle Ltd. Recruitment Brochure

A 12pp A4 portrait brochure is required. It should have a contemporary and modern feel to it.

Please feel free to bring the flow chart to life with symbols that reflect the title of the stage in the flow chart.

Similarly the services that are offered should be brought to life.

See the attached brief for the detailed copy and brand colour details. I have also attached the logo and imagery to be used although we are open to additional / alternative imagery as long as it is royalty free and won't cost any additional money.

Target Market(s)

Small and medium sized businesses

Industry/Entity Type

Recruitment

Font styles to use
Serif
Sans Serif

Requirements
Must have
• See project brief.
Nice to have
• See project brief - bringing the flow chart and services aspects to life would be good.
Should not have
• See project brief.

```html
<!DOCTYPE html>
<html lang="en">
<head>
<meta charset="utf-8">
<title>Corwen Haddle Ltd. – Why Use Us</title>
<link href="https://fonts.googleapis.com/css2?family=Montserrat:wght@400;500;600;700&display=swap" rel="stylesheet">
<style>
  :root{
    --backdrop:#e6e3df;
    --paper:#ffffff;
    --maroon:#7a1d3c;
    --accent:#b3325e;
    --slate:#6a6b70;
    --ink-light:#ffffff;
    --rule:#8a2346;
    --muted:#9a9a9e;
    --plum-top:#8f2150;
    --plum-bottom:#5c1230;
  }
  *{box-sizing:border-box;margin:0;padding:0}
  html,body{width:1200px;height:900px;overflow:hidden;background:var(--backdrop)}
  body{font-family:'Montserrat',sans-serif;position:relative}
  .spread{position:absolute;left:20px;top:40px;width:1160px;height:820px;display:flex;box-shadow:0 6px 24px rgba(0,0,0,.18)}
  .page{position:relative;width:580px;height:820px;background:var(--paper);overflow:hidden}
  .page-header{position:absolute;left:0;right:0;top:0;height:68px;border-bottom:2px solid var(--rule)}
  .page-number{position:absolute;top:44px;font-size:10px;font-weight:500;color:#333}
  .edge-mark{position:absolute;top:4px;width:1px;height:56px;background:#333}
  .brand-mark{position:absolute;top:32px;display:flex;align-items:center;gap:6px;font-size:15px;font-weight:700;color:var(--maroon);letter-spacing:.5px}
  .brand-mark .dot{width:10px;height:10px;border-radius:50%;background:var(--maroon)}
  .running-title{position:absolute;top:46px;font-size:9.5px;font-weight:600;color:var(--maroon);letter-spacing:.4px}
  .page-title{position:absolute;top:92px;left:0;width:580px;text-align:center;font-size:22px;font-weight:700;color:var(--maroon);letter-spacing:.5px;padding-left:0}
  .intro-panel{position:absolute;left:0;top:169px;width:324px;height:624px;background:var(--slate);padding:108px 24px 0 27px;color:var(--ink-light)}
  .intro-panel p{font-size:9px;line-height:11.8px;margin-bottom:11px}
  .lead{color:#c4416e}
  .photo{position:absolute;top:169px;height:624px}
  .photo-left{left:324px;width:256px;background:linear-gradient(100deg,#2b2b2e 0%,#55565a 18%,#e9ecee 45%,#f3f4f5 70%,#c9c3bd 100%)}
  .photo-right{left:0;width:580px;background:linear-gradient(100deg,#d4d6d7 0%,#f2f3f4 30%,#e3e5e6 55%,#b9bcbe 75%,#d7d2cb 100%)}
  .benefits-panel{position:absolute;right:0;top:169px;width:235px;height:489px;background:linear-gradient(180deg,var(--plum-top),var(--plum-bottom));padding:30px 16px 0 32px;color:var(--ink-light)}
  .benefits-panel h2{font-size:17px;font-weight:500;line-height:21px;margin-bottom:24px}
  .benefit{margin-bottom:13px}
  .benefit h3{font-size:10.5px;font-weight:600;margin-bottom:2px}
  .benefit p{font-size:8.6px;line-height:11.3px}
  .benefit.small h3{font-size:9px}
</style>
</head>
<body>
<div class="spread">
  <section class="page page-left">
    <header class="page-header">
      <span class="edge-mark" style="left:26px"></span>
      <span class="page-number" style="left:34px">3</span>
      <div class="brand-mark" style="left:58px"><span class="dot"></span>CORWEN HADDLE</div>
      <span class="running-title" style="left:430px">CORWEN HADDLE</span>
    </header>
    <h1 class="page-title">WHY USE US?</h1>
    <div class="intro-panel">
      <p><span class="lead">We pride ourselves</span> on our ability to deliver on every assignment and are specialists in senior sales recruitment and headhunting across a wide spectrum of roles. And we know that no two roles are the same which is why we offer a range of recruitment and headhunting services to deliver to your needs.</p>
      <p><span class="lead">But we also</span> know the challenges of the recruitment process. Our Managing Director, Alan Pryce, has been on the client side of this process and set up Corwen Haddle after identifying a real need for a truly professional sales recruitment and headhunting service.</p>
      <p><span class="lead">Alan felt huge</span> frustration at the approach taken by many sales recruitment agencies when he was on the client side. This has ensured a commitment to embedding a quality service ethos from the top down and that is why we undertake a detailed proven approach on every assignment we take on.</p>
      <p><span class="lead">We take an</span> empathetic approach and work in partnership with organisations to headhunt the best performing senior sales talent who will help to build profitable growth. Having considerable experience of sourcing and building effective sales teams, we fully recognise the importance of recruiting the correct calibre of senior sales people. We know how to spot candidates with the correct industry experience, demonstrable track record and a desire to succeed.</p>
      <p><span class="lead">We know the</span> top performing senior people are not usually looking for a role because their existing employer makes sure they are kept happy. But we are specialists in identifying, approaching and delivering that talent for our clients.</p>
    </div>
    <div class="photo photo-left" role="img" aria-label="Photograph, left half: two businessmen in suits seated in a bright office by tall windows, talking"></div>
  </section>

  <section class="page page-right">
    <header class="page-header">
      <div class="brand-mark" style="left:58px"><span class="dot"></span>CORWEN HADDLE</div>
      <span class="running-title" style="left:430px">CORWEN HADDLE</span>
      <span class="page-number" style="left:538px">4</span>
      <span class="edge-mark" style="left:552px"></span>
    </header>
    <div class="photo photo-right" role="img" aria-label="Photograph, right half: a young businessman seated on a chair in a bright office with tall windows and a patterned carpet"></div>
    <aside class="benefits-panel">
      <h2>What’s more,<br>we also provide:</h2>
      <div class="benefit"><h3>• Total confidentiality</h3><p>you can be sure we will operate in a strictly confidential manner in relation to both the candidates we contact as well as within your own organisation.</p></div>
      <div class="benefit"><h3>• Dedicated contact</h3><p>you will be provided with a dedicated contact who will provide you with regular updates as often as you would like.</p></div>
      <div class="benefit"><h3>• Full transparency</h3><p>through the headhunting process, you get complete visibility at every stage so you will know the lengths we have gone to in order to exceed your expectations</p></div>
      <div class="benefit"><h3>• Complete accountability</h3><p>we will not rest until we have found you the best available person for your role.</p></div>
      <div class="benefit small"><h3>• Extended 12 month free of</h3><p>charge replacement guarantee on headhunting assignments where we undertake competency interviews alongside you.</p></div>
    </aside>
  </section>
</div>
</body>
</html>
```